Lumen Cove Skincare - Package Design

New Beauty label needing product packaging design. Looking for elegant and stylish design to represent our premium brand.

This project is for 1 label and 1 box design. The winning designer will be assigned another project for the next product in the range. (to be paid as a new project)

This product is for "Dead Sea Mud Mask". Please see the label format and jar attached. Please note there are 2 different jars we are considering (will have a mud inside). Please feel free to choose whichever one suits your design best.

The labels and boxes are to retain the product information, such as size, ingredients etc, but is to be updated to our brand. You can move or display the other information as you wish.

the size of the dead sea mud mask color box is 72*72*85mm (length*width*height)
the size of dead sea mud mask label is 218*58mm (width*height)

Target Market(s)

Women 15 to 65

Requirements
Must have
• Must be elegant and represent our brand which is a premium beauty product.
Should not have
• Dark blue. Dark purple etc. Colours should compliment the logo

```html
<!DOCTYPE html>
<html lang="en">
<head>
<meta charset="utf-8">
<title>Lumen Cove Skincare – Dead Sea Mud Mix Packaging</title>
<link rel="stylesheet" href="https://fonts.googleapis.com/css2?family=Montserrat:wght@400;500;600&family=Oswald:wght@500;600&display=swap">
<style>
  :root {
    --page: #ececec;
    --board: #151515;
    --board-edge: #2a2a2a;
    --fold: #4a4a4a;
    --gold: #c9a24a;
    --white: #f4f1ea;
    --muted: #a7a39a;
    --teal: #3f8288;
    --teal-deep: #1d3f44;
  }
  * { box-sizing: border-box; margin: 0; padding: 0; }
  html, body { width: 720px; height: 1200px; overflow: hidden; }
  body { background: var(--page); position: relative; font-family: "Montserrat", sans-serif; color: var(--white); }

  .brand { display: flex; align-items: center; justify-content: center; gap: 5px; }
  .brand-dot { width: 9px; height: 9px; border: 1px solid var(--gold); border-radius: 50%; }
  .brand-name { font-family: "Montserrat", sans-serif; font-weight: 500; color: var(--gold); font-size: 10px; letter-spacing: .5px; white-space: nowrap; }

  .product-title { font-family: "Oswald", sans-serif; font-weight: 600; color: var(--white); letter-spacing: 1px; text-align: center; border-top: 1px solid var(--gold); border-bottom: 1px solid var(--gold); padding: 2px 0; }
  .benefits { font-size: 5px; color: var(--white); text-align: center; margin-top: 3px; letter-spacing: .3px; }
  .claim { font-size: 4.5px; color: var(--muted); text-align: center; margin-top: 4px; }
  .vitamins { font-size: 4.5px; color: var(--teal); text-align: center; margin-top: 2px; font-weight: 600; letter-spacing: .3px; }
  .volume { font-size: 5px; color: var(--white); text-align: center; margin-top: 3px; }

  .info-heading { font-family: "Oswald", sans-serif; font-weight: 500; font-size: 7px; color: var(--gold); letter-spacing: .8px; margin-bottom: 3px; }
  .info-text { font-size: 5px; line-height: 1.5; color: var(--muted); }

  .wave-band { position: absolute; left: 0; right: 0; bottom: 0; background: linear-gradient(180deg, rgba(21,21,21,0) 0%, var(--teal-deep) 45%, var(--teal) 100%); opacity: .85; }

  .care-icons { display: flex; gap: 4px; margin-top: 6px; }
  .care-icon { width: 9px; height: 9px; border: 1px solid var(--muted); border-radius: 50%; }

  /* Label */
  .label { position: absolute; left: 60px; top: 185px; width: 600px; height: 160px; background: var(--board); overflow: hidden; display: grid; grid-template-columns: 200px 200px 200px; }
  .label-section { position: relative; padding: 16px 18px; z-index: 1; }
  .label-center { display: flex; flex-direction: column; align-items: center; padding-top: 18px; }
  .label-center .brand-name { font-size: 13px; }
  .label-center .brand-dot { width: 11px; height: 11px; }
  .label-center .product-title { font-size: 17px; margin-top: 12px; width: 170px; }
  .label .wave-band { height: 34px; z-index: 0; }

  /* Box dieline */
  .dieline { position: absolute; left: 28px; top: 445px; width: 664px; height: 570px; }
  .dieline svg { position: absolute; inset: 0; }
  .face { position: absolute; overflow: hidden; }
  .side-panel { top: 190px; width: 160px; height: 190px; padding: 16px 14px; }
  .front-panel { top: 190px; width: 160px; height: 190px; display: flex; flex-direction: column; align-items: center; padding-top: 18px; }
  .front-panel .product-title { font-size: 14px; margin-top: 12px; width: 134px; }
  .dieline .wave-band { height: 32px; }
  .lid-face { width: 160px; height: 160px; display: flex; flex-direction: column; align-items: center; justify-content: center; }
  .lid-face .brand-name { font-size: 11px; }
</style>
</head>
<body>

<section class="label" aria-label="Jar label">
  <div class="label-section">
    <h3 class="info-heading">DIRECTIONS</h3>
    <p class="info-text">Apply an even layer to clean, damp skin. Leave on for ten minutes, then rinse with warm water. Use twice weekly.</p>
    <p class="info-text" style="margin-top:4px">Store in a cool dry place. For external use only.</p>
  </div>
  <div class="label-section label-center">
    <div class="brand"><span class="brand-dot"></span><span class="brand-name">Lumen Cove Skincare</span></div>
    <h1 class="product-title">DEAD SEA MUD MIX</h1>
    <p class="benefits">Anti-Acne · Deep Skin Cleanse · Pore Reducer</p>
    <p class="claim">100% Natural Minerals · Infused Beneficial Extracts</p>
    <p class="vitamins">WITH VITAMINS &amp; MINERALS FOR HEALTHY SKIN</p>
    <p class="volume">250ML / 8.5FL OZ</p>
  </div>
  <div class="label-section">
    <h3 class="info-heading">INGREDIENTS</h3>
    <p class="info-text">Dead Sea mud, kaolin, aloe leaf juice, glycerin, vitamin E, chamomile extract.</p>
    <div class="care-icons"><span class="care-icon"></span><span class="care-icon"></span><span class="care-icon"></span></div>
  </div>
  <div class="wave-band" role="img" aria-label="Teal ocean wave pattern along the base"></div>
</section>

<section class="dieline" aria-label="Box dieline">
  <svg width="664" height="570" viewBox="0 0 664 570" aria-hidden="true">
    <g fill="#151515" stroke="#2a2a2a" stroke-width="1">
      <polygon points="24,198 0,212 0,360 24,372"/>
      <path d="M24 190 L28 126 Q30 114 44 114 L168 120 L184 190 Z"/>
      <path d="M344 190 L348 126 Q350 114 364 114 L488 120 L504 190 Z"/>
      <rect x="184" y="30" width="160" height="160"/>
      <path d="M184 30 Q188 0 214 0 L314 0 Q340 0 344 30 Z"/>
      <rect x="24" y="190" width="640" height="190"/>
      <path d="M24 380 L28 444 Q30 456 44 456 L168 450 L184 380 Z"/>
      <path d="M344 380 L348 444 Q350 456 364 456 L488 450 L504 380 Z"/>
      <rect x="504" y="380" width="160" height="160"/>
      <path d="M504 540 Q508 570 534 570 L634 570 Q660 570 664 540 Z"/>
    </g>
    <g stroke="#4a4a4a" stroke-width="1" stroke-dasharray="3 3">
      <line x1="184" y1="190" x2="184" y2="380"/>
      <line x1="344" y1="190" x2="344" y2="380"/>
      <line x1="504" y1="190" x2="504" y2="380"/>
      <line x1="24" y1="190" x2="24" y2="380"/>
    </g>
  </svg>

  <div class="face side-panel" style="left:24px">
    <h3 class="info-heading">DIRECTIONS</h3>
    <p class="info-text">Apply an even layer to clean, damp skin. Leave on for ten minutes, then rinse with warm water. Use twice weekly.</p>
    <div class="wave-band" role="img" aria-label="Teal ocean wave pattern along the base"></div>
  </div>

  <div class="face front-panel" style="left:184px">
    <div class="brand"><span class="brand-dot"></span><span class="brand-name">Lumen Cove Skincare</span></div>
    <h2 class="product-title">DEAD SEA MUD MIX</h2>
    <p class="benefits">Anti-Acne · Deep Skin Cleanse · Pore Reducer</p>
    <p class="claim">100% Natural Minerals · Infused Beneficial Extracts</p>
    <p class="vitamins">WITH VITAMINS &amp; MINERALS FOR HEALTHY SKIN</p>
    <p class="volume">250ML / 8.5FL OZ</p>
    <div class="wave-band" role="img" aria-label="Teal ocean wave pattern along the base"></div>
  </div>

  <div class="face side-panel" style="left:344px">
    <h3 class="info-heading">INGREDIENTS</h3>
    <p class="info-text">Dead Sea mud, kaolin, aloe leaf juice, glycerin, vitamin E, chamomile extract.</p>
    <p class="info-text" style="margin-top:4px">Store in a cool dry place. For external use only.</p>
    <div class="wave-band" role="img" aria-label="Teal ocean wave pattern along the base"></div>
  </div>

  <div class="face front-panel" style="left:504px">
    <div class="brand"><span class="brand-dot"></span><span class="brand-name">Lumen Cove Skincare</span></div>
    <h2 class="product-title">DEAD SEA MUD MIX</h2>
    <p class="benefits">Anti-Acne · Deep Skin Cleanse · Pore Reducer</p>
    <div class="care-icons"><span class="care-icon"></span><span class="care-icon"></span><span class="care-icon"></span></div>
    <p class="volume">250ML / 8.5FL OZ</p>
    <div class="wave-band" role="img" aria-label="Teal ocean wave pattern along the base"></div>
  </div>

  <div class="face lid-face" style="left:184px; top:30px">
    <div class="brand"><span class="brand-dot"></span><span class="brand-name">Lumen Cove Skincare</span></div>
  </div>
</section>

</body>
</html>
```